Request for Business Card Design

Hi. My name is Marlena, I am looking for a new business card design for my company, Quillbrook Sensing Systems, LLC. I really like the design you did for Tavel Harvest and was hoping you could do something similar using our full logo and our mark. I am also open to any raised texture design using our mark. I have attached our full logo, which would need to be somewhere on the card, as well as the mark in both outline and full form, as well as our brand colors / guide. The card does not have to be white, as long as our logo and mark appear. I actually like darker colored business cards more, but am open to all options. If you are interested in working with me, please let me know. We would also take the business card design into letterhead design if you can do that.

```html
<!DOCTYPE html>
<html lang="en">
<head>
<meta charset="utf-8">
<title>Quillbrook Sensing Systems — Business Card</title>
<link href="https://fonts.googleapis.com/css2?family=Lato:wght@400;700;900&display=swap" rel="stylesheet">
<style>
  :root {
    --bg: #1f2023;
    --card: #3b3c3f;
    --teal: #1e7089;
    --teal-bright: #0d95c4;
    --white: #f4f5f6;
    --muted: #d8dadc;
    --rule: #8a8c8f;
  }
  * { margin: 0; padding: 0; box-sizing: border-box; }
  html, body { width: 1200px; height: 952px; overflow: hidden; }
  body {
    background: var(--bg);
    font-family: "Lato", sans-serif;
    color: var(--white);
    position: relative;
  }
  .card {
    position: absolute;
    left: 280px;
    width: 640px;
    height: 366px;
    background: var(--card);
    border-radius: 28px;
    overflow: hidden;
    box-shadow: 0 14px 30px rgba(0,0,0,.45);
  }
  .card--front { top: 64px; }
  .card--back { top: 522px; }

  /* front */
  .brand {
    position: absolute; left: 96px; top: 40px;
    display: flex; align-items: center; gap: 12px;
  }
  .brand__dot { width: 34px; height: 34px; border-radius: 50%; background: var(--teal-bright); }
  .brand__name { font-weight: 900; font-size: 26px; letter-spacing: 2px; line-height: 1; color: var(--white); }
  .brand__tag { font-weight: 900; font-size: 8.5px; letter-spacing: 1.2px; color: var(--white); margin-top: 4px; }

  .side-rule { position: absolute; left: 40px; top: 60px; width: 1.5px; height: 250px; background: var(--rule); }

  .contacts { position: absolute; left: 70px; top: 130px; list-style: none; }
  .contacts li { display: flex; align-items: flex-start; gap: 10px; font-size: 13px; line-height: 1.35; margin-bottom: 9px; color: var(--muted); }
  .contacts svg { flex: none; margin-top: 1px; }

  .person { position: absolute; right: 70px; top: 150px; text-align: right; }
  .person__name { font-weight: 900; font-size: 24px; letter-spacing: 1.5px; }
  .person__name .surname { color: var(--teal-bright); }
  .person__title { font-size: 16px; margin-top: 4px; color: var(--muted); }
  .accent-square { position: absolute; right: 0; top: 150px; width: 42px; height: 62px; background: var(--teal-bright); }

  .front-mark { position: absolute; right: 150px; bottom: -70px; width: 200px; height: 200px; border-radius: 50%; background: var(--teal); }

  /* back */
  .back-mark { position: absolute; left: 70px; top: 78px; width: 210px; height: 210px; border-radius: 50%; background: var(--teal); }
  .back-brand { position: absolute; left: 310px; top: 150px; }
  .back-brand__name { font-weight: 900; font-size: 40px; letter-spacing: 3px; line-height: 1; }
  .back-brand__tag { font-weight: 900; font-size: 12px; letter-spacing: 2px; margin-top: 8px; }
</style>
</head>
<body>

<section class="card card--front" aria-label="Business card, contact side">
  <div class="side-rule"></div>

  <div class="brand">
    <span class="brand__dot"></span>
    <div>
      <div class="brand__name">QUILLBROOK</div>
      <div class="brand__tag">SENSING SYSTEMS, LLC</div>
    </div>
  </div>

  <ul class="contacts">
    <li>
      <svg width="16" height="16" viewBox="0 0 16 16"><rect width="16" height="16" rx="2" fill="var(--teal-bright)"/><path d="M8 3.5a3 3 0 0 0-3 3c0 2.2 3 5.5 3 5.5s3-3.3 3-5.5a3 3 0 0 0-3-3zm0 4.2a1.2 1.2 0 1 1 0-2.4 1.2 1.2 0 0 1 0 2.4z" fill="#fff"/></svg>
      <span>212 Alder Crossing Road<br>Fernvale, OR 97402</span>
    </li>
    <li>
      <svg width="16" height="16" viewBox="0 0 16 16"><rect width="16" height="16" rx="2" fill="var(--teal-bright)"/><path d="M5.2 3.5l1.6 2.2-1 1.1a6 6 0 0 0 3.4 3.4l1.1-1 2.2 1.6-.9 1.7c-3.9-.3-7.2-3.6-7.5-7.5z" fill="#fff"/></svg>
      <span>+00 555 218 40</span>
    </li>
    <li>
      <svg width="16" height="16" viewBox="0 0 16 16"><rect width="16" height="16" rx="2" fill="var(--teal-bright)"/><rect x="3.5" y="5" width="9" height="6.5" fill="none" stroke="#fff" stroke-width="1.2"/><path d="M3.5 5l4.5 3.6L12.5 5" fill="none" stroke="#fff" stroke-width="1.2"/></svg>
      <span>hello@quillbrooksensing.com</span>
    </li>
    <li>
      <svg width="16" height="16" viewBox="0 0 16 16"><rect width="16" height="16" rx="2" fill="var(--teal-bright)"/><circle cx="8" cy="8" r="4.3" fill="none" stroke="#fff" stroke-width="1.2"/><path d="M3.7 8h8.6M8 3.7c-2 2.3-2 6.3 0 8.6M8 3.7c2 2.3 2 6.3 0 8.6" fill="none" stroke="#fff" stroke-width="1"/></svg>
      <span>www.quillbrooksensing.com</span>
    </li>
  </ul>

  <div class="person">
    <div class="person__name">MARLENA C. <span class="surname">OKAFOR</span></div>
    <div class="person__title">Managing Director</div>
  </div>
  <div class="accent-square"></div>

  <div class="front-mark"></div>
</section>

<section class="card card--back" aria-label="Business card, logo side">
  <div class="back-mark"></div>
  <div class="back-brand">
    <div class="back-brand__name">QUILLBROOK</div>
    <div class="back-brand__tag">SENSING SYSTEMS, LLC</div>
  </div>
</section>

</body>
</html>
```